Travel Blogger Business Card for roamquill.net

I need a two-sided business card for a travel blogging website. The card should be both professional and fun at the same time. This is for the website www.roamquill.net

I don't necessarily think that the current logo on the website needs to be used on the business card but it can be. I am very flexible with ideas

Target Market(s)

Travel agencies that will be met at a conference.

Industry/Entity Type

Travel

Contact Information for Business Card

Company Name: Roam Quill.net
Name: Bertrand Olesky
Voice: +1-(345)-402-7731
Address: Coral Reach Shore, Grand Cayman, Cayman Islands
Email: ceo@roamquill.net

Colors
0592cd
0355a3
3176b5
33a6d7
85cae6
85acd3

Requirements
Must have
• Website address and name should be bigger than address, phone number, and email.

```html
<!DOCTYPE html>
<html lang="en">
<head>
<meta charset="utf-8">
<title>Roam Quill.net – Business Card</title>
<link rel="stylesheet" href="https://fonts.googleapis.com/css2?family=Montserrat:wght@600;700&family=Didact+Gothic&display=swap">
<style>
  :root {
    --stage: #e9e7e3;
    --teal: #1d4952;
    --teal-deep: #143840;
    --skyline: #0d2329;
    --paper: #f4f3f0;
    --paper-map: #e4e3df;
    --ink-teal: #1f4d57;
    --ink-soft: #3d5b62;
    --white: #ffffff;
  }
  * { margin: 0; padding: 0; box-sizing: border-box; }
  html, body { width: 1200px; height: 561px; overflow: hidden; }
  body {
    background: var(--stage);
    display: flex;
    align-items: center;
    justify-content: center;
    gap: 50px;
    font-family: "Didact Gothic", "Century Gothic", sans-serif;
  }
  .card {
    position: relative;
    width: 525px;
    height: 300px;
    overflow: hidden;
    box-shadow: 0 6px 18px rgba(0,0,0,0.18);
  }

  /* Front */
  .card-front { background: var(--teal); color: var(--white); }
  .front-map {
    position: absolute; inset: 0;
    background: radial-gradient(ellipse at 55% 40%, #255761 0%, var(--teal) 55%, var(--teal-deep) 100%);
  }
  .brand {
    position: absolute;
    left: 0; right: 0; top: 88px;
    text-align: center;
  }
  .brand-name {
    display: inline-flex;
    align-items: center;
    gap: 14px;
    font-family: "Montserrat", sans-serif;
    font-weight: 700;
    font-size: 34px;
    letter-spacing: 1px;
    color: var(--white);
  }
  .brand-dot {
    width: 30px; height: 30px;
    border-radius: 50%;
    background: var(--white);
  }
  .brand-url {
    margin-top: 6px;
    font-family: "Montserrat", sans-serif;
    font-weight: 600;
    font-size: 17px;
    letter-spacing: 4.5px;
    color: var(--white);
  }
  .front-skyline {
    position: absolute;
    left: 0; right: 0; bottom: 0;
    height: 62px;
    background: linear-gradient(180deg, rgba(13,35,41,0) 0%, var(--skyline) 45%, var(--skyline) 100%);
  }

  /* Back */
  .card-back { background: var(--paper); color: var(--ink-teal); }
  .back-map {
    position: absolute; inset: 0;
    background: radial-gradient(ellipse at 40% 50%, var(--paper-map) 0%, var(--paper) 70%);
  }
  .back-skyline {
    position: absolute;
    top: 0; right: 0; bottom: 0;
    width: 64px;
    background: linear-gradient(270deg, var(--teal) 0%, var(--teal) 55%, rgba(29,73,82,0) 100%);
  }
  .holder-name {
    position: absolute;
    left: 34px; top: 38px;
    font-size: 40px;
    letter-spacing: 0.5px;
    color: var(--ink-teal);
  }
  .contact-list {
    position: absolute;
    left: 36px; top: 118px;
    list-style: none;
    font-size: 14px;
    color: var(--ink-soft);
  }
  .contact-list li {
    display: flex;
    align-items: flex-start;
    gap: 12px;
    margin-bottom: 11px;
    line-height: 1.35;
  }
  .contact-icon { width: 16px; height: 16px; flex: none; margin-top: 1px; fill: var(--ink-teal); }
  .contact-web { font-size: 16px; color: var(--ink-teal); }
</style>
</head>
<body>

  <section class="card card-front" aria-label="Card front">
    <div class="front-map" role="img" aria-label="Faint vintage world map texture"></div>
    <div class="brand">
      <div class="brand-name"><span class="brand-dot"></span>ROAM QUILL</div>
      <div class="brand-url">www.roamquill.net</div>
    </div>
    <div class="front-skyline" role="img" aria-label="Silhouette skyline of world landmarks"></div>
  </section>

  <section class="card card-back" aria-label="Card back">
    <div class="back-map" role="img" aria-label="Faint light world map texture"></div>
    <div class="back-skyline" role="img" aria-label="Vertical silhouette skyline of world landmarks"></div>
    <h1 class="holder-name">Bertrand Olesky</h1>
    <ul class="contact-list">
      <li>
        <svg class="contact-icon" viewBox="0 0 16 16" aria-hidden="true"><path d="M4 1h8a1 1 0 0 1 1 1v12a1 1 0 0 1-1 1H4a1 1 0 0 1-1-1V2a1 1 0 0 1 1-1zm1 2v9h6V3H5zm3 10.2a.8.8 0 1 0 0-.01z"/></svg>
        <span>+1-(345)-402-7731</span>
      </li>
      <li>
        <svg class="contact-icon" viewBox="0 0 16 16" aria-hidden="true"><path d="M8 1a5 5 0 0 1 5 5c0 3.6-5 9-5 9S3 9.6 3 6a5 5 0 0 1 5-5zm0 3a2 2 0 1 0 0 4 2 2 0 0 0 0-4z"/></svg>
        <span>Coral Reach Shore, Grand Cayman,<br>Cayman Islands.</span>
      </li>
      <li>
        <svg class="contact-icon" viewBox="0 0 16 16" aria-hidden="true"><path d="M1 3h14v10H1V3zm1.5 1.3V12h11V4.3L8 8.6 2.5 4.3zM3.3 4 8 7.6 12.7 4H3.3z"/></svg>
        <span>ceo@roamquill.net</span>
      </li>
      <li>
        <svg class="contact-icon" viewBox="0 0 16 16" aria-hidden="true"><path d="M8 1a7 7 0 1 1 0 14A7 7 0 0 1 8 1zm-5.5 6.3h2.6c.1-1.7.5-3.2 1.2-4.3A5.6 5.6 0 0 0 2.5 7.3zm4 0h3c-.1-1.8-.7-3.3-1.5-4.3-.8 1-1.4 2.5-1.5 4.3zm4.4 0h2.6A5.6 5.6 0 0 0 9.7 3c.7 1.1 1.1 2.6 1.2 4.3zM2.5 8.7a5.6 5.6 0 0 0 3.8 4.3c-.7-1.1-1.1-2.6-1.2-4.3H2.5zm4 0c.1 1.8.7 3.3 1.5 4.3.8-1 1.4-2.5 1.5-4.3h-3zm4.4 0c-.1 1.7-.5 3.2-1.2 4.3a5.6 5.6 0 0 0 3.8-4.3h-2.6z"/></svg>
        <span class="contact-web">www.roamquill.net</span>
      </li>
    </ul>
  </section>

</body>
</html>
```